Birchway Inspection website (same layout, different look/style)

I want to create a NEW website based off the wordpress layout of another website. I want to have the same functionality/layout but a totally different look and style. I want my new website to have the same layout and features but to look totally different (different fonts, different logo, different colors, different style).

In the files section I have included different examples of the style I am looking for. That is conservative, trusted, simple, elegant and a little boring. I am trying to have the style of an insurnace company or bank website.

Please use that kind of style but use the same wordpress layout as the target website above.

Colors: blue, grey, green

You can use the same copy, I will add that later during the project.

My company is Birchway Inspections
birchwayinspections-example.com
tel:
(941) 555-0187
address:
4173 Quillmoor Ave,
Sarasota, FL 34299

Target Market(s)

Inspection

Industry/Entity Type

Inspection

Number of Pages Required

3 page

Font styles to use
Sans Serif

Colors
0054AA
0677BA
7BADD7
CADEEF
E8F1F8
0094D4
00A9DD
6FCCEA
C7EBF8
E9F6FB

Requirements
Must have
• Landing page, services page, about page

```html
<!DOCTYPE html>
<html lang="en">
<head>
<meta charset="utf-8">
<title>Birchway Inspections</title>
<link rel="stylesheet" href="https://fonts.googleapis.com/css2?family=IBM+Plex+Sans:ital,wght@0,300;0,400;0,500;0,600;0,700;1,400&display=swap">
<style>
:root{
  --navy:#0b2a4a;
  --blue-deep:#0054AA;
  --blue:#0677BA;
  --blue-soft:#7BADD7;
  --blue-pale:#CADEEF;
  --blue-mist:#E8F1F8;
  --green:#2f8a5b;
  --green-soft:#dcefe4;
  --grey-50:#f4f6f8;
  --grey-200:#d9dee4;
  --grey-500:#6b7480;
  --ink:#1c2733;
  --text:#4a5562;
  --white:#fff;
}
*{box-sizing:border-box;margin:0;padding:0}
html,body{width:1200px;height:3185px;overflow:hidden}
body{font-family:"IBM Plex Sans",sans-serif;color:var(--ink);background:var(--white);position:relative}
section,header,footer{position:absolute;left:0;width:1200px}
.btn{position:absolute;display:flex;align-items:center;justify-content:center;gap:8px;border-radius:3px;font-weight:500;font-size:14px;letter-spacing:.3px;text-decoration:none}
.btn-blue{background:var(--blue-deep);color:var(--white)}
.btn-green{background:var(--green);color:var(--white)}
.btn-outline{background:transparent;color:var(--blue-deep);border:1.5px solid var(--blue-deep)}
.chev{width:10px;height:10px}

/* header */
.site-header{top:0;height:113px;background:var(--white);border-bottom:1px solid var(--grey-200)}
.topbar{position:absolute;left:0;top:0;width:1200px;height:37px;background:var(--navy)}
.topbar-links{position:absolute;right:100px;top:0;height:37px;display:flex;align-items:center;gap:14px;color:var(--white);font-size:13px;font-weight:400;letter-spacing:.3px}
.topbar-links .sep{width:1px;height:16px;background:rgba(255,255,255,.3)}
.topbar-links .phone{display:flex;align-items:center;gap:7px;font-weight:500}
.icon-row{display:flex;gap:6px}
.icon-row span{width:26px;height:26px;border-radius:50%;border:1px solid rgba(255,255,255,.45);display:flex;align-items:center;justify-content:center}
.brand{position:absolute;left:100px;top:51px;display:flex;align-items:center;gap:12px}
.brand-mark{width:36px;height:36px;background:var(--green);border-radius:4px}
.brand-name{font-weight:600;font-size:24px;color:var(--navy);line-height:1}
.brand-sub{font-weight:400;font-size:11px;letter-spacing:2.2px;color:var(--grey-500);margin-top:5px}
.nav{position:absolute;left:449px;top:66px;display:flex;gap:34px;font-size:15px;font-weight:500;color:var(--ink)}
.nav .active{color:var(--blue-deep);box-shadow:inset 0 -2px 0 var(--green);padding-bottom:6px}
.site-header .btn{left:882px;top:56px;width:216px;height:40px}

/* hero */
.hero{top:113px;height:626px;background:linear-gradient(90deg,rgba(11,42,74,.95) 0%,rgba(11,42,74,.75) 45%,rgba(74,96,122,.55) 100%),linear-gradient(180deg,#7d8aa3 0%,#4d5a70 55%,#2e3338 100%)}
.hero-kicker{position:absolute;left:100px;top:160px;width:48px;height:3px;background:var(--green)}
.hero-title{position:absolute;left:100px;top:185px;font-size:46px;font-weight:600;line-height:54px;color:var(--white)}
.hero-copy{position:absolute;left:100px;top:310px;width:440px;font-size:16px;line-height:27px;color:#dbe6f1;font-weight:300}
.hero .btn{left:101px;top:384px;width:216px;height:44px}

/* services */
.services{top:739px;height:586px;background:var(--grey-50)}
.section-title{position:absolute;left:0;width:1200px;text-align:center;font-size:34px;font-weight:600;color:var(--navy)}
.section-rule{position:absolute;left:576px;width:48px;height:3px;background:var(--green)}
.card{position:absolute;top:128px;width:311px;height:389px;background:var(--white);border:1px solid var(--grey-200);text-align:center}
.card-photo{height:196px;width:100%;border-bottom:4px solid var(--green)}
.card h3{position:absolute;top:228px;width:100%;font-size:21px;font-weight:600;color:var(--navy)}
.card p{position:absolute;top:268px;left:22px;right:22px;font-size:13.5px;line-height:22px;color:var(--text);font-weight:300}
.card .more{position:absolute;top:342px;width:100%;display:flex;justify-content:center;align-items:center;gap:6px;font-size:14px;font-weight:500;color:var(--blue-deep)}

/* about */
.about{top:1325px;height:531px;background:var(--blue-mist)}
.about-photo{position:absolute;left:100px;top:78px;width:455px;height:377px;background:linear-gradient(135deg,#c9d2da 0%,#8e8172 55%,#4e463f 100%);box-shadow:14px 14px 0 var(--blue-pale)}
.about h2{position:absolute;left:655px;top:104px;font-size:34px;font-weight:600;color:var(--navy)}
.about .accent{position:absolute;left:655px;top:152px;width:48px;height:3px;background:var(--green)}
.about p{position:absolute;left:655px;top:168px;width:445px;font-size:14.5px;line-height:27px;color:var(--text);font-weight:300}
.about .btn{left:655px;top:377px;width:157px;height:40px}

/* testimonials */
.testimonials{top:1856px;height:488px}
.quote-card{position:absolute;top:139px;width:436px;height:255px;background:var(--white);border:1px solid var(--grey-200);border-left:4px solid var(--blue-deep)}
.quote-mark{position:absolute;left:27px;top:24px}
.quote-card p{position:absolute;left:27px;top:80px;width:385px;font-size:14.5px;line-height:26px;color:var(--text);font-weight:300;font-style:italic}
.avatar{position:absolute;left:27px;top:172px;width:58px;height:58px;border-radius:50%;background:linear-gradient(135deg,var(--blue-soft),#7a828c)}
.who{position:absolute;left:102px;top:184px}
.who strong{display:block;font-size:17px;font-weight:600;color:var(--navy)}
.who em{font-size:13px;color:var(--grey-500);font-style:normal}
.slider-arrow{position:absolute;top:238px;width:42px;height:42px;border:1px solid var(--grey-200);border-radius:50%;display:flex;align-items:center;justify-content:center}
.dots{position:absolute;top:422px;left:554px;display:flex;gap:14px}
.dots span{width:10px;height:10px;border-radius:50%;background:var(--grey-200)}
.dots .on{background:var(--green)}

/* contact */
.contact{top:2344px;height:512px;background:var(--navy)}
.contact-photo{position:absolute;left:0;top:0;width:440px;height:512px;background:linear-gradient(160deg,#9aa4ae 0%,#7a6f63 55%,#4b4540 100%)}
.contact h2{position:absolute;left:494px;top:64px;font-size:38px;font-weight:600;color:var(--white)}
.contact .accent{position:absolute;left:494px;top:114px;width:48px;height:3px;background:var(--green)}
.field{position:absolute;background:var(--white);border-radius:3px;font-size:14.5px;color:var(--grey-500);padding:12px 15px;font-weight:300}
.contact .btn{left:494px;top:399px;width:156px;height:42px}

/* footer */
.site-footer{top:2856px;height:329px;background:#0f1c2b;color:var(--white)}
.foot-brand{position:absolute;left:103px;top:64px;display:flex;align-items:center;gap:14px}
.foot-brand .brand-mark{width:46px;height:46px}
.foot-brand .brand-name{color:var(--white);font-size:32px}
.foot-brand .brand-sub{color:var(--blue-soft);font-size:13px}
.foot-icons{position:absolute;left:103px;top:210px;display:flex;gap:12px}
.foot-icons span{width:38px;height:38px;border-radius:50%;border:1px solid rgba(255,255,255,.35);display:flex;align-items:center;justify-content:center}
.foot-col{position:absolute;top:64px}
.foot-col h4{font-size:17px;font-weight:600;margin-bottom:12px}
.foot-col li{list-style:none;font-size:14px;line-height:31px;font-weight:300;color:#c6d0db}
.foot-col address{font-style:normal;font-size:14px;line-height:21px;font-weight:300;color:#c6d0db}
.foot-col address span{display:block;margin-bottom:10px}
.foot-rule{position:absolute;left:100px;top:274px;width:1000px;height:1px;background:rgba(255,255,255,.15)}
.copyright{position:absolute;top:292px;width:1200px;text-align:center;font-size:14px;font-weight:300;color:#9aa7b5}
</style>
</head>
<body>

<header class="site-header">
  <div class="topbar">
    <div class="topbar-links">
      <span>Client Login</span><span class="sep"></span>
      <span>Pay Online</span><span class="sep"></span>
      <span class="phone"><svg width="13" height="13" viewBox="0 0 24 24"><path d="M6.6 10.8a15 15 0 0 0 6.6 6.6l2.2-2.2a1 1 0 0 1 1-.25 11.4 11.4 0 0 0 3.6.57 1 1 0 0 1 1 1V20a1 1 0 0 1-1 1A17 17 0 0 1 3 4a1 1 0 0 1 1-1h3.5a1 1 0 0 1 1 1c0 1.25.2 2.45.57 3.57a1 1 0 0 1-.25 1z" fill="#fff"/></svg>(941) 555-0187</span><span class="sep"></span>
      <span class="icon-row">
        <span><svg width="12" height="12" viewBox="0 0 24 24" fill="none" stroke="#fff" stroke-width="2"><rect x="3" y="5" width="18" height="14" rx="1"/><path d="M3 6l9 7 9-7"/></svg></span>
        <span><svg width="12" height="12" viewBox="0 0 24 24" fill="none" stroke="#fff" stroke-width="2"><circle cx="12" cy="12" r="9"/><path d="M3 12h18M12 3c3 3 3 15 0 18M12 3c-3 3-3 15 0 18"/></svg></span>
        <span><svg width="12" height="12" viewBox="0 0 24 24" fill="none" stroke="#fff" stroke-width="2"><path d="M4 5h16v11H9l-5 4z"/></svg></span>
        <span><svg width="12" height="12" viewBox="0 0 24 24" fill="none" stroke="#fff" stroke-width="2"><path d="M12 21s-7-6.5-7-12a7 7 0 0 1 14 0c0 5.5-7 12-7 12z"/><circle cx="12" cy="9" r="2.5"/></svg></span>
      </span>
    </div>
  </div>
  <div class="brand">
    <span class="brand-mark"></span>
    <div><div class="brand-name">Birchway</div><div class="brand-sub">INSURANCE INSPECTIONS</div></div>
  </div>
  <nav class="nav">
    <span class="active">Home</span><span>About</span><span>Service</span><span>Contact</span>
  </nav>
  <a class="btn btn-green">Request Inspection <svg class="chev" viewBox="0 0 10 10"><path d="M3 1.5 6.5 5 3 8.5" stroke="#fff" stroke-width="1.6" fill="none"/></svg></a>
</header>

<section class="hero" role="img" aria-label="City skyline with lit towers reflected on a river at dusk">
  <div class="hero-kicker"></div>
  <h1 class="hero-title">Birchway Insurance<br>Inspections</h1>
  <p class="hero-copy">Lorem ipsum dolor sit amet, consecscing elit, sed do eiusmod tempor incididunt ut labore et dolore magna aliqua.</p>
  <a class="btn btn-green">Request Inspection <svg class="chev" viewBox="0 0 10 10"><path d="M3 1.5 6.5 5 3 8.5" stroke="#fff" stroke-width="1.6" fill="none"/></svg></a>
</section>

<section class="services">
  <h2 class="section-title" style="top:52px">Our Services</h2>
  <div class="section-rule" style="top:104px"></div>
  <article class="card" style="left:100px">
    <div class="card-photo" role="img" aria-label="Inspector working on a grey shingle roof" style="background:linear-gradient(180deg,#d9dde2,#8a8f94)"></div>
    <h3>Wind Mitigation</h3>
    <p>Lorem ipsum dolor sit amet, cur adipiscing elit, sed smod tempor incididunt ut labore et dolore magna aliqua.</p>
    <div class="more">Learn More <svg class="chev" viewBox="0 0 10 10"><path d="M3 1.5 6.5 5 3 8.5" stroke="#0054AA" stroke-width="1.6" fill="none"/></svg></div>
  </article>
  <article class="card" style="left:445px">
    <div class="card-photo" role="img" aria-label="Man in glasses reviewing a document at a desk" style="background:linear-gradient(180deg,#dfe3e6,#4a6280)"></div>
    <h3>Four Point Inspection</h3>
    <p>Lorem ipsum dolor sit amet, cur adipiscing elit, sed smod tempor incididunt ut labore et dolore magna aliqua.</p>
    <div class="more">Learn More <svg class="chev" viewBox="0 0 10 10"><path d="M3 1.5 6.5 5 3 8.5" stroke="#0054AA" stroke-width="1.6" fill="none"/></svg></div>
  </article>
  <article class="card" style="left:789px">
    <div class="card-photo" role="img" aria-label="Team reviewing a house model over blueprints" style="background:linear-gradient(180deg,#5a5e64,#e6e8ea)"></div>
    <h3>Roof Certification</h3>
    <p>Lorem ipsum dolor sit amet, cur adipiscing elit, sed smod tempor incididunt ut labore et dolore magna aliqua.</p>
    <div class="more">Learn More <svg class="chev" viewBox="0 0 10 10"><path d="M3 1.5 6.5 5 3 8.5" stroke="#0054AA" stroke-width="1.6" fill="none"/></svg></div>
  </article>
</section>

<section class="about">
  <div class="about-photo" role="img" aria-label="Handshake over a contract beside a small model house"></div>
  <h2>About Us</h2>
  <div class="accent"></div>
  <p>Sed ut perspiciatis unde omnisatusor sit voluptatem accusantium doloremque laudantium, totam rem apiam, eaque ipsa quae ab illo inventore veritatis et quasi architecto beatae vitae dicta sunt explicabo. Nemo enim ipsam voluptauia voluptas sit aspernatur aut odit aut fugit, sed quia consequuntur magni dolores eos qui ratione voluptatem sequi nesciunt. Neque porro quisquam est, qui dolorem ipsum quia dolor</p>
  <a class="btn btn-blue">Learn More <svg class="chev" viewBox="0 0 10 10"><path d="M3 1.5 6.5 5 3 8.5" stroke="#fff" stroke-width="1.6" fill="none"/></svg></a>
</section>

<section class="testimonials">
  <h2 class="section-title" style="top:60px">What Our Clients Say</h2>
  <div class="section-rule" style="top:112px"></div>
  <span class="slider-arrow" style="left:78px"><svg width="18" height="14" viewBox="0 0 18 14"><path d="M17 7H2M7 1 1 7l6 6" stroke="#1c2733" stroke-width="1.6" fill="none"/></svg></span>
  <article class="quote-card" style="left:142px">
    <svg class="quote-mark" width="34" height="28" viewBox="0 0 50 44"><path d="M2 22C2 10 9 3 20 1v8c-5 2-8 6-8 11h8v22H2zM28 22C28 10 35 3 46 1v8c-5 2-8 6-8 11h8v22H28z" fill="#2f8a5b"/></svg>
    <p>Lorem ipsum dolor sit amet, consecttgcing elit, sed do eiusmod tempor incididunt ut labore et dolore maga aliqua. Quis ipsum suspendisse ultrices gravida...</p>
    <div class="avatar" role="img" aria-label="Client portrait"></div>
    <div class="who"><strong>John Doe</strong><em>Standard Lorem</em></div>
  </article>
  <article class="quote-card" style="left:622px">
    <svg class="quote-mark" width="34" height="28" viewBox="0 0 50 44"><path d="M2 22C2 10 9 3 20 1v8c-5 2-8 6-8 11h8v22H2zM28 22C28 10 35 3 46 1v8c-5 2-8 6-8 11h8v22H28z" fill="#2f8a5b"/></svg>
    <p>Lorem ipsum dolor sit amet, consecttgcing elit, sed do eiusmod tempor incididunt ut labore et dolore maga aliqua. Quis ipsum suspendisse ultrices gravida...</p>
    <div class="avatar" role="img" aria-label="Client portrait"></div>
    <div class="who"><strong>John Doe</strong><em>Standard Lorem</em></div>
  </article>
  <span class="slider-arrow" style="left:1080px"><svg width="18" height="14" viewBox="0 0 18 14"><path d="M1 7h15M11 1l6 6-6 6" stroke="#1c2733" stroke-width="1.6" fill="none"/></svg></span>
  <div class="dots"><span></span><span class="on"></span><span></span><span></span></div>
</section>

<section class="contact">
  <div class="contact-photo" role="img" aria-label="Inspector in hard hat and safety vest holding a tablet beside a roof gutter"></div>
  <h2>Get In Touch</h2>
  <div class="accent"></div>
  <div class="field" style="left:494px;top:134px;width:293px;height:44px">Full Name</div>
  <div class="field" style="left:807px;top:134px;width:294px;height:44px">Company</div>
  <div class="field" style="left:494px;top:201px;width:293px;height:44px">Email</div>
  <div class="field" style="left:807px;top:201px;width:294px;height:44px">Phone</div>
  <div class="field" style="left:494px;top:267px;width:607px;height:106px">Full Name</div>
  <a class="btn btn-green">Submit <svg class="chev" viewBox="0 0 10 10"><path d="M3 1.5 6.5 5 3 8.5" stroke="#fff" stroke-width="1.6" fill="none"/></svg></a>
</section>

<footer class="site-footer">
  <div class="foot-brand">
    <span class="brand-mark"></span>
    <div><div class="brand-name">Birchway</div><div class="brand-sub">INSURANCE INSPECTIONS</div></div>
  </div>
  <div class="foot-icons">
    <span><svg width="16" height="16" viewBox="0 0 24 24" fill="none" stroke="#fff" stroke-width="1.8"><rect x="3" y="5" width="18" height="14" rx="1"/><path d="M3 6l9 7 9-7"/></svg></span>
    <span><svg width="16" height="16" viewBox="0 0 24 24" fill="none" stroke="#fff" stroke-width="1.8"><path d="M6.6 10.8a15 15 0 0 0 6.6 6.6l2.2-2.2a1 1 0 0 1 1-.25 11.4 11.4 0 0 0 3.6.57 1 1 0 0 1 1 1V20a1 1 0 0 1-1 1A17 17 0 0 1 3 4a1 1 0 0 1 1-1h3.5a1 1 0 0 1 1 1c0 1.25.2 2.45.57 3.57a1 1 0 0 1-.25 1z"/></svg></span>
    <span><svg width="16" height="16" viewBox="0 0 24 24" fill="none" stroke="#fff" stroke-width="1.8"><path d="M12 21s-7-6.5-7-12a7 7 0 0 1 14 0c0 5.5-7 12-7 12z"/><circle cx="12" cy="9" r="2.5"/></svg></span>
    <span><svg width="16" height="16" viewBox="0 0 24 24" fill="none" stroke="#fff" stroke-width="1.8"><circle cx="12" cy="12" r="9"/><path d="M3 12h18M12 3c3 3 3 15 0 18M12 3c-3 3-3 15 0 18"/></svg></span>
  </div>
  <div class="foot-col" style="left:484px">
    <h4>Quick Links</h4>
    <ul><li>Home</li><li>About</li><li>Services</li><li>Contact</li></ul>
  </div>
  <div class="foot-col" style="left:691px">
    <h4>Other Links</h4>
    <ul><li>Contact Sales</li><li>Legal Hub</li><li>Privacy Policy</li><li>Trust &amp; Security</li><li>Cookie Preferences</li></ul>
  </div>
  <div class="foot-col" style="left:880px">
    <h4>Contact Info</h4>
    <address><span>4173 Quillmoor Ave,<br>Sarasota, FL 34299</span><span>(941) 555-0187</span><span>info@birchwayinspections-example.com</span></address>
  </div>
  <div class="foot-rule"></div>
  <p class="copyright">©Copyright 2024 Birchway Inspections. All Rights Reserved.</p>
</footer>

</body>
</html>
```